Organic Food Producer Needs Business Card

We need an attractive business card that is both trendy and professional. We are a FQRB, Vetra Clear Certified organic producer of coconut oil, coconut flour and additional cacao products. We produce some of the world's purest coconut oil and coconut oil derived products in the world.
We take pride in the purity of our products and the transparency with which we create our products. Use of FQRB Organic and Vetra Clear logos is acceptable and preferred. The final design would reflect our values for purity and the natural state of our products.
The business card should include: job title, email address, phone number and facebook, twitter, instagram tag.
Don't be afraid to get creative! I have attached some of our packaging design in JPG format as well as our logo. The jpgs dont display the colors correctly in chrome but they will display correctly if you DL and open them in photoshop.
Target Market(s)
Cards likely to be used in organic food industry events for people such as buyers, trade show reps, etc... but also store owners and people casually interested in.
The company's target market :
Primary:
Women - 22-65. Women typically hold the household budget and make the purchasing decisions at the supermarket. They are interested in quality healthy and beauty products at a good value. Organic, fair trade, artisanally made are all important attributes of brands they purchase. They try to maintain a healthy lifestyle through proper eating, exercise and work/life balance.
Secondary:
Men - 44% of American adults are single so it is important to note that men will also be a key target audience. And they too are concerned and passionate about organic, fair trade, artisanally made, good value and living a healthy lifestyle.
Tertiary:
Health & Wellness Professionals (Nutritionists, Doctors, etc) Coconut is highly nutritional and more and more, it is being recommended as part of a healthy diet by professionals. We should keep this audience in mind as well, particularly when we build a website with useful resources such as the company’s high standards, the health benefits of coconut, nutrition info and recipes.
Industry/Entity Type
Business
Requirements
Must have
- Pretty open minded about creativity and variety, I do like the color palettes in the labeling files provided... but it is not a deal breaker to vary from this.
Should be visually impacting.
Nice to have
- Would like to have some creative use of raised lettering or detail.
Should not have
- Although the company is based in the caribbean, we are not looking for an overly ethnic caribbean feel.
You should open the attached files in photoshop, as they seem to distort the color in a web browser.

```html
<!DOCTYPE html>
<html lang="en">
<head>
<meta charset="utf-8">
<title>Coral Husk — Business Card</title>
<link rel="stylesheet" href="https://fonts.googleapis.com/css2?family=Open+Sans:wght@400;600;700&display=swap">
<style>
  :root {
    --bg: #ece9e4;
    --ink: #0b0b0c;
    --teal: #1f8fa6;
    --teal-deep: #17788c;
    --sky: #9fd6e2;
    --cream: #f6e7c4;
    --white: #ffffff;
    --text-dark: #2b2b2b;
    --shell-light: #f3f1ee;
    --shell-mid: #d9cfc4;
    --shell-brown: #b89a7c;
  }
  * { box-sizing: border-box; margin: 0; padding: 0; }
  html, body {
    width: 1200px; height: 720px; overflow: hidden;
    background: var(--bg);
    font-family: "Open Sans", Arial, sans-serif;
  }
  .stage {
    position: relative; width: 1200px; height: 720px;
    display: flex; align-items: center; justify-content: center; gap: 50px;
  }
  .card {
    position: relative; width: 540px; height: 309px; overflow: hidden;
    box-shadow: 0 6px 18px rgba(0,0,0,.18);
  }

  /* Front */
  .card-front { background: var(--ink); }
  .card-front .waves { position: absolute; inset: 0; width: 100%; height: 100%; }
  .brand {
    position: absolute; display: flex; align-items: center; gap: 10px;
  }
  .brand-dot {
    width: 26px; height: 26px; border-radius: 50%; background: var(--teal);
    flex: none;
  }
  .brand-name {
    font-weight: 700; color: var(--teal); letter-spacing: .5px; line-height: 1;
  }
  .card-front .brand { left: 52px; top: 48px; }
  .card-front .brand-name { font-size: 34px; }
  .person { position: absolute; left: 52px; top: 128px; }
  .person-name { color: var(--teal); font-weight: 700; font-size: 17px; }
  .person-name .title { font-weight: 400; font-size: 14px; }
  .address { margin-top: 14px; color: var(--white); font-size: 12.5px; line-height: 1.5; }
  .contacts {
    position: absolute; right: 30px; top: 110px; list-style: none;
    color: var(--white); font-size: 13px; line-height: 1.55;
  }
  .contacts li { display: flex; align-items: center; gap: 7px; }
  .contacts svg { width: 12px; height: 12px; flex: none; }

  /* Back */
  .card-back { background: var(--shell-light); }
  .photo-fill {
    position: absolute; inset: 0;
    background:
      radial-gradient(ellipse 40% 45% at 42% 35%, #ffffff 0%, rgba(255,255,255,0) 70%),
      radial-gradient(ellipse 45% 50% at 70% 60%, var(--shell-brown) 0%, rgba(184,154,124,0) 70%),
      radial-gradient(ellipse 35% 40% at 20% 80%, var(--shell-mid) 0%, rgba(217,207,196,0) 70%),
      linear-gradient(135deg, #eef0f2, #e6dcd1);
    opacity: .75;
  }
  .back-content {
    position: absolute; inset: 0; display: flex; flex-direction: column;
    align-items: center; justify-content: center; gap: 18px;
  }
  .card-back .brand { position: static; }
  .card-back .brand-dot { width: 36px; height: 36px; }
  .card-back .brand-name { font-size: 50px; }
  .web { color: var(--text-dark); font-size: 18px; font-weight: 600; letter-spacing: 4px; }
</style>
</head>
<body>
<main class="stage">

  <section class="card card-front" aria-label="Business card front">
    <svg class="waves" viewBox="0 0 540 309" preserveAspectRatio="none" aria-hidden="true">
      <path d="M0,238 C140,282 250,222 330,138 C395,72 460,48 540,46 L540,309 L0,309 Z" fill="var(--cream)"/>
      <path d="M0,250 C140,294 252,234 334,150 C398,84 462,60 540,58 L540,309 L0,309 Z" fill="var(--ink)"/>
      <path d="M0,262 C140,304 256,246 338,162 C402,96 464,72 540,70 L540,309 L0,309 Z" fill="var(--sky)"/>
      <path d="M0,276 C150,312 262,258 344,176 C408,110 468,86 540,84 L540,309 L0,309 Z" fill="var(--teal)"/>
    </svg>

    <div class="brand">
      <span class="brand-dot"></span>
      <span class="brand-name">Coral Husk</span>
    </div>

    <div class="person">
      <p class="person-name">Your Name, <span class="title">Title</span></p>
      <p class="address">Street Name, City Name<br>Zip Code-00000</p>
    </div>

    <ul class="contacts">
      <li>
        <svg viewBox="0 0 12 12"><circle cx="6" cy="6" r="5.3" fill="none" stroke="#fff" stroke-width="1.2"/><path d="M4 3.5 L5 3.5 L5.5 5 L4.8 5.6 C5.2 6.5 5.6 7 6.4 7.3 L7 6.6 L8.5 7 L8.5 8 C6 8.3 3.8 6 4 3.5 Z" fill="#fff"/></svg>
        012-555-0148
      </li>
      <li>
        <svg viewBox="0 0 12 12"><rect x="3.5" y="1" width="5" height="10" rx="1" fill="#fff"/><rect x="4.3" y="2.2" width="3.4" height="6.6" fill="var(--teal)"/></svg>
        012-555-0148
      </li>
      <li>
        <svg viewBox="0 0 12 12"><rect x="1" y="2.5" width="10" height="7" rx="1" fill="#fff"/><path d="M1.5 3 L6 6.5 L10.5 3" fill="none" stroke="var(--teal)" stroke-width="1"/></svg>
        admin@coralhusk.com
      </li>
      <li>
        <svg viewBox="0 0 12 12"><circle cx="6" cy="6" r="5" fill="#fff"/><path d="M1 6 H11 M6 1 C3.5 3.5 3.5 8.5 6 11 M6 1 C8.5 3.5 8.5 8.5 6 11" fill="none" stroke="var(--teal)" stroke-width=".8"/></svg>
        www.coralhusk.com
      </li>
    </ul>
  </section>

  <section class="card card-back" aria-label="Business card back">
    <div class="photo-fill" role="img" aria-label="Softly faded photograph of a cracked-open coconut"></div>
    <div class="back-content">
      <div class="brand">
        <span class="brand-dot"></span>
        <span class="brand-name">Coral Husk</span>
      </div>
      <p class="web">www.coralhusk.com</p>
    </div>
  </section>

</main>
</body>
</html>
```